Business Card Design for Event Planning Company

Create a business card for event planning company using our new logo. After I pick the design, I will need files made for 6 employees. Our company provides event design & logistics services as well as venue management. The font should be sans serif and complementary to the logo. I will need to know the name of the font selected for the final design. The phone numbers listed should be separated by "." not "-"

Address for the card
PO Box 318, Washington, DC 20019

Card One
Lorna Pettibone
lpettibone@galavoyant.com
202.481.7730

Card Two
Miriam Okonkwo
mokonkwo@galavoyant.com
202.556.2047

Card Three
Tessa Varnholt
tvarnholt@galavoyant.com
978.620.4471

Card Four
Robin Fess
rfess@galavoyant.com
202.718.3362

Card Five
Ada-Rose Pelletan-Uzor
adarose@galavoyant.com
202.839.1205

Card Six
Beatrix Holloway
Beatrix@galavoyant.com
202.492.6618

Target Market(s)

Corporate/Non-Profit

Industry/Entity Type

Event Planning

Contact Information for Business Card

Address for the card

Card One
Lorna Pettibone
lpettibone@galavoyant.com
202.481.7730

Card Two
Miriam Okonkwo
202.556.2047

Card Three
Tessa Varnholt
978.620.4471

Card Four
Robin Fess
rfess@galavoyant.com
202.718.3362

Card Five
Ada-Rose Pelletan-Uzor
202.839.1205

Card Six
Beatrix Holloway
202.492.6618

Font styles to use
Sans Serif

Colors

Designer to choose colors to be used in the design.

Requirements
Must have
• Two-sided with logo
Should not have
• Extra colors or be too busy

```html
<!DOCTYPE html>
<html lang="en">
<head>
<meta charset="utf-8">
<title>Galavoyant business card concepts</title>
<link href="https://fonts.googleapis.com/css2?family=Jost:wght@400;500;600&family=Oswald:wght@500;600&display=swap" rel="stylesheet">
<style>
  :root {
    --teal: #5ea7a7;
    --teal-light: #8cc1c1;
    --teal-accent: #7cb8b8;
    --ink: #0c0c0c;
    --paper: #ffffff;
    --grey: #5e5e5e;
    --sans: "Jost", "Futura", sans-serif;
    --condensed: "Oswald", "Arial Narrow", sans-serif;
  }
  * { margin: 0; padding: 0; box-sizing: border-box; }
  html, body { width: 927px; height: 1200px; overflow: hidden; background: var(--paper); }
  body { position: relative; font-family: var(--sans); color: var(--ink); }

  .column-label { position: absolute; top: 25px; font-size: 10px; font-weight: 600; letter-spacing: 3px; }
  .row-number { position: absolute; left: 37px; font-size: 10px; font-weight: 600; }

  .card { position: absolute; width: 380px; height: 217px; overflow: hidden; }
  .card.front { left: 55px; border: 2px solid var(--ink); background: var(--paper); }
  .card.back { left: 487px; background: var(--teal); color: var(--ink); }
  .card.rounded { border-radius: 14px; }

  .centered { position: absolute; left: 0; right: 0; text-align: center; }

  .brand { display: flex; flex-direction: column; align-items: center; gap: 6px; }
  .brand-dot { border-radius: 50%; background: var(--teal); }
  .brand-name { font-weight: 400; color: var(--ink); line-height: 1; }

  .name { font-weight: 500; }
  .tagline { font-weight: 600; font-size: 10px; color: var(--paper); letter-spacing: .2px; }
  .address-line { font-size: 11.5px; letter-spacing: .4px; }

  .tag-band { position: absolute; left: 0; right: 0; top: 96px; height: 24px; border-top: 1px solid var(--teal-light); border-bottom: 1px solid var(--teal-light); display: flex; align-items: center; justify-content: center; }

  .contact-band { position: absolute; left: 0; right: 0; bottom: 0; height: 90px; background: var(--ink); color: var(--paper); font-size: 12.5px; line-height: 16.5px; }
  .contact-band .col { position: absolute; top: 12px; }

  .side-panel { position: absolute; right: 0; top: 0; bottom: 0; width: 113px; background: var(--teal); color: var(--paper); padding: 80px 0 0 10px; font-size: 14px; line-height: 18px; }

  .card.back.statement { background: var(--ink); }
  .statement svg { display: block; width: 380px; height: 217px; }
  .statement-line { font-family: var(--condensed); font-weight: 600; font-size: 40px; fill: var(--grey); }
  .statement-line .accent { fill: var(--teal-accent); }

  .condensed-tag { font-family: var(--condensed); font-weight: 500; font-size: 18px; letter-spacing: 2px; line-height: 24px; color: var(--paper); }

  .footer-band { position: absolute; left: 0; right: 0; bottom: 0; height: 38px; background: var(--ink); color: var(--paper); display: flex; align-items: center; justify-content: center; font-family: var(--condensed); font-weight: 500; font-size: 13px; letter-spacing: .4px; }
</style>
</head>
<body>

<div class="column-label" style="left:223px">FRONT</div>
<div class="column-label" style="left:657px">BACK</div>

<!-- Row 1 -->
<div class="row-number" style="top:58px">1</div>
<div class="card front" style="top:42px">
  <div class="centered brand" style="top:50px">
    <span class="brand-dot" style="width:40px;height:40px"></span>
    <span class="brand-name" style="font-size:46px">galavoyant</span>
  </div>
</div>
<div class="card back" style="top:42px">
  <div class="centered" style="top:32px;font-size:14px;line-height:18px">
    <div class="name">Lorna Pettibone</div>
    <div>lpettibone@galavoyant.com</div>
    <div>202.481.7730</div>
  </div>
  <div class="centered tagline" style="top:113px">A LEADING EVENT LOGISTICS &amp; VENUE MANAGEMENT FIRM</div>
  <div class="centered address-line" style="top:180px">PO Box 318 · Washington, DC 20019 · galavoyant.com</div>
</div>

<!-- Row 2 -->
<div class="row-number" style="top:275px">2</div>
<div class="card front" style="top:267px">
  <div class="centered brand" style="top:70px">
    <span class="brand-dot" style="width:34px;height:34px"></span>
    <span class="brand-name" style="font-size:38px">galavoyant</span>
  </div>
</div>
<div class="card back" style="top:267px">
  <div class="centered" style="top:36px;font-size:14px;line-height:19px">
    <div class="name">Lorna Pettibone</div>
    <div>lpettibone@galavoyant.com</div>
  </div>
  <div class="tag-band"><span class="tagline">A LEADING EVENT LOGISTICS &amp; VENUE MANAGEMENT FIRM</span></div>
  <div class="centered name" style="top:150px;font-size:14px;font-weight:600">202.481.7730</div>
  <div class="centered address-line" style="top:189px">PO Box 318 · Washington, DC 20019 · galavoyant.com</div>
</div>

<!-- Row 3 -->
<div class="row-number" style="top:507px">3</div>
<div class="card front" style="top:492px">
  <div class="centered brand" style="top:18px">
    <span class="brand-dot" style="width:36px;height:36px"></span>
    <span class="brand-name" style="font-size:40px">galavoyant</span>
  </div>
  <div class="contact-band">
    <div class="col" style="left:19px">
      <div class="name" style="color:var(--teal)">Lorna Pettibone</div>
      <div>lpettibone@galavoyant.com</div>
      <div>202.481.7730</div>
    </div>
    <div class="col" style="left:211px;color:#cfcfcf;letter-spacing:.4px">
      <div>PO Box 318</div>
      <div>Washington, DC 20019</div>
      <div>galavoyant.com</div>
    </div>
  </div>
</div>
<div class="card back" style="top:492px">
  <div class="centered condensed-tag" style="top:84px">A LEADING EVENT LOGISTICS<br>AND VENUE MANAGEMENT FIRM</div>
</div>

<!-- Row 4 -->
<div class="row-number" style="top:729px">4</div>
<div class="card front" style="top:718px">
  <div class="brand" style="position:absolute;left:0;width:267px;top:34px">
    <span class="brand-dot" style="width:32px;height:32px"></span>
    <span class="brand-name" style="font-size:36px">galavoyant</span>
  </div>
  <div style="position:absolute;left:101px;top:138px;font-size:12px;line-height:14.5px">
    <div>PO Box 318</div>
    <div>Washington, DC 20019</div>
    <div>galavoyant.com</div>
    <div>lpettibone@galavoyant.com</div>
  </div>
  <div class="side-panel">
    <div class="name">Lorna Pettibone</div>
    <div>202.481.7730</div>
  </div>
</div>
<div class="card back statement" style="top:718px">
  <svg viewBox="0 0 380 217" aria-label="Washington DC’s premier event logistics and venue management firm">
    <text class="statement-line" x="15" y="53" textLength="352" lengthAdjust="spacingAndGlyphs">WASHINGTON DC’S</text>
    <text class="statement-line" x="15" y="102" textLength="354" lengthAdjust="spacingAndGlyphs">PREMIER <tspan class="accent">EVENT</tspan></text>
    <text class="statement-line" x="15" y="152" textLength="354" lengthAdjust="spacingAndGlyphs">LOGISTICS AND VENUE</text>
    <text class="statement-line" x="15" y="202" textLength="354" lengthAdjust="spacingAndGlyphs">MANAGEMENT FIRM</text>
  </svg>
</div>

<!-- Row 5 -->
<div class="row-number" style="top:960px">5</div>
<div class="card front rounded" style="top:943px">
  <div class="centered brand" style="top:52px;flex-direction:row;justify-content:center;gap:14px">
    <span class="brand-dot" style="width:72px;height:72px"></span>
    <span class="brand-name" style="font-size:58px;line-height:72px">galavoyant</span>
  </div>
</div>
<div class="card back rounded" style="top:943px;background:var(--paper);border:2px solid var(--ink)">
  <div class="centered brand" style="top:6px;gap:4px">
    <span class="brand-dot" style="width:30px;height:30px"></span>
    <span class="brand-name" style="font-size:31px">galavoyant</span>
  </div>
  <div class="centered" style="top:86px;font-size:13px;line-height:16px">
    <div class="name">Lorna Pettibone</div>
    <div style="font-weight:600">202.481.7730</div>
  </div>
  <div class="centered" style="top:128px;font-size:12px;line-height:15.5px;letter-spacing:.3px">
    <div>PO Box 318 · Washington, DC 20019</div>
    <div>galavoyant.com</div>
    <div>lpettibone@galavoyant.com</div>
  </div>
  <div class="footer-band">A LEADING EVENT LOGISTICS &amp; VENUE MANAGEMENT FIRM</div>
</div>

</body>
</html>
```